8" x 11" One Page Flyer for Fence Installation Company

We are looking to promote our business with a new flyer that would be handed out in person to people or put at their mailbox/door at their homes. The flyer needs to be creative and attention-grabbing. I have attached some of our previous flyers and our website information. Do not call or email regarding the flyer. We want the flyer to look professional but also friendly. One page, NOT folded. You can use images from our website at www.MyBraxtonYard.com or our Facebook page at www.Facebook.com/HollowbrookRailsBKT. We are flexible with what photos you can use but there must be photos of OUR fences on the flyer. More photos specifically can also be provided. Colors need to be suitable for a flyer printed on canary yellow in color paper OR white paper.

Target Market(s)

Homeowners that need a new fence

Industry/Entity Type

Construction

Font styles to use
Sans Serif
Other font styles liked:
• HD Colton

Colors
0054AA
0677BA
7BADD7
CADEEF
E8F1F8
0094D4
00A9DD
6FCCEA
C7EBF8
E9F6FB

Requirements
Must have
• Our fence photos - mostly wood fence photos (different designs), SIZE SHOULD BE LETTER SIZE 8" x 11"
Nice to have
• A nice bible verse featured at the bottom of the flyer.
Should not have
• DO NOT COPY THE WEBSITE FORMAT, I WANT SOMETHING UNIQUE. Other people's fence photos, they must all come from our website or facebook page

```html
<!DOCTYPE html>
<html lang="en">
<head>
<meta charset="utf-8">
<title>Hollowbrook Rails – Flyer</title>
<link rel="stylesheet" href="https://fonts.googleapis.com/css2?family=Montserrat:wght@400;500;600;700;800&display=swap">
<style>
  :root{
    --orange:#e8832a;
    --orange-dark:#d9701a;
    --ink:#222222;
    --muted:#555555;
    --paper:#ffffff;
    --backdrop:#e8e8e8;
    --brand-blue:#0677ba;
    --pin:#d83a2a;
  }
  *{margin:0;padding:0;box-sizing:border-box}
  html,body{width:1200px;height:792px;overflow:hidden}
  body{background:var(--backdrop);font-family:"Montserrat",sans-serif;color:var(--ink);position:relative}

  .sheet{position:absolute;top:46px;width:540px;height:700px;background:var(--paper);overflow:hidden;box-shadow:0 2px 10px rgba(0,0,0,.12)}
  .sheet--front{left:40px}
  .sheet--back{left:620px}
  .sheet svg.art{position:absolute;inset:0}

  /* front */
  .brand{position:absolute;left:44px;top:292px;display:flex;align-items:center;gap:7px}
  .brand__mark{width:28px;height:28px;background:var(--orange-dark)}
  .brand__name{font-size:14px;font-weight:600;color:var(--brand-blue);line-height:1}
  .brand__phone{font-size:15px;font-weight:700;color:var(--ink);margin-top:3px}
  .brand__tag{position:absolute;left:44px;top:330px;font-size:6.5px;color:var(--muted);width:170px}
  .headline{position:absolute;left:30px;top:346px;font-size:19px;font-weight:800;letter-spacing:.2px}
  .subline{position:absolute;left:30px;top:370px;font-size:9px;font-weight:500;color:var(--ink)}
  .contact{position:absolute;left:0;right:0;top:610px;text-align:center;color:#fff;font-weight:600;line-height:1.25}
  .contact__phone{font-size:19px;font-weight:700}
  .contact__line{font-size:17px}

  /* back */
  .why{position:absolute;left:26px;top:60px;font-size:28px;font-weight:800;color:var(--orange)}
  .why__sub{position:absolute;left:26px;top:96px;width:300px;font-size:11px;color:var(--ink);text-align:center;line-height:1.35}
  .perks{position:absolute;left:40px;top:148px;width:330px;list-style:none;text-align:center}
  .perks li{font-size:12.5px;font-weight:500;height:24px;line-height:24px}
  .perks li::before{content:"";display:inline-block;width:6px;height:6px;border-radius:50%;background:var(--orange);margin-right:8px;vertical-align:middle}
  .where{position:absolute;left:0;width:545px;top:374px;text-align:center;font-size:16px;font-weight:700;color:var(--orange)}
  .visit{position:absolute;left:20px;width:400px;top:590px;text-align:center;color:#fff;font-size:9.5px;line-height:1.35}
  .visit__title{font-weight:700;font-size:10.5px}
  .visit__big{font-size:20px;font-weight:800;vertical-align:-2px}
  .visit__hours{font-weight:700}
</style>
</head>
<body>

<section class="sheet sheet--front" aria-label="Flyer front">
  <svg class="art" viewBox="0 0 540 700" width="540" height="700">
    <defs>
      <linearGradient id="yardWash" x1="0" y1="0" x2="0" y2="1">
        <stop offset="0" stop-color="#f4f4f4"/>
        <stop offset=".45" stop-color="#ecebe7"/>
        <stop offset="1" stop-color="#e3e3e0"/>
      </linearGradient>
      <linearGradient id="woodSky" x1="0" y1="0" x2="0" y2="1">
        <stop offset="0" stop-color="#9fb9cf"/><stop offset=".45" stop-color="#c9a46a"/><stop offset="1" stop-color="#6f8a45"/>
      </linearGradient>
      <linearGradient id="skyFence" x1="0" y1="0" x2="0" y2="1">
        <stop offset="0" stop-color="#b9d0e6"/><stop offset=".55" stop-color="#9ea3a6"/><stop offset="1" stop-color="#7d8b66"/>
      </linearGradient>
      <linearGradient id="ironLawn" x1="0" y1="0" x2="0" y2="1">
        <stop offset="0" stop-color="#6f7478"/><stop offset=".5" stop-color="#2f3236"/><stop offset="1" stop-color="#667f3e"/>
      </linearGradient>
      <linearGradient id="picketHouse" x1="0" y1="0" x2="1" y2="1">
        <stop offset="0" stop-color="#8f969c"/><stop offset=".45" stop-color="#e0c38e"/><stop offset="1" stop-color="#c9a46a"/>
      </linearGradient>
      <linearGradient id="gateBrick" x1="0" y1="0" x2="0" y2="1">
        <stop offset="0" stop-color="#9a5a44"/><stop offset=".4" stop-color="#d4b27c"/><stop offset="1" stop-color="#a8844f"/>
      </linearGradient>
      <linearGradient id="blackLawn" x1="0" y1="0" x2="0" y2="1">
        <stop offset="0" stop-color="#c8d8e4"/><stop offset=".45" stop-color="#2c2f33"/><stop offset="1" stop-color="#5f8a35"/>
      </linearGradient>
      <linearGradient id="archGate" x1="0" y1="0" x2="0" y2="1">
        <stop offset="0" stop-color="#5f8a35"/><stop offset=".4" stop-color="#d0ad74"/><stop offset="1" stop-color="#b48a52"/>
      </linearGradient>
      <linearGradient id="railBrick" x1="0" y1="0" x2="0" y2="1">
        <stop offset="0" stop-color="#a2bfd6"/><stop offset=".35" stop-color="#9a5c45"/><stop offset=".65" stop-color="#d8bb86"/><stop offset="1" stop-color="#a58a62"/>
      </linearGradient>
      <linearGradient id="privacyShrubs" x1="0" y1="0" x2="1" y2="1">
        <stop offset="0" stop-color="#8fae68"/><stop offset=".5" stop-color="#c9a46a"/><stop offset="1" stop-color="#4f6e2e"/>
      </linearGradient>
      <linearGradient id="railLawn" x1="0" y1="0" x2="0" y2="1">
        <stop offset="0" stop-color="#4f6e2e"/><stop offset=".5" stop-color="#b9935c"/><stop offset="1" stop-color="#6f8f3f"/>
      </linearGradient>
    </defs>
    <rect role="img" aria-label="Faded photo of a backyard patio enclosed by a white fence" x="0" y="0" width="540" height="590" fill="url(#yardWash)"/>
    <g class="fence-photos" stroke="#ffffff" stroke-width="4">
      <polygon role="img" aria-label="Photo of a wooden picket gate" fill="url(#woodSky)" points="272,70 243,120 185,120 156,70 185,20 243,20"/>
      <polygon role="img" aria-label="Photo of a tall privacy fence under a blue sky" fill="url(#skyFence)" points="185,121 152.5,177 87.5,177 55,121 87.5,65 152.5,65"/>
      <polygon role="img" aria-label="Photo of a black metal fence" fill="url(#ironLawn)" points="275,168 252.5,207 207.5,207 185,168 207.5,129 252.5,129"/>
      <polygon role="img" aria-label="Photo of a long wooden picket fence beside a house" fill="url(#picketHouse)" points="481,148 425.5,244 314.5,244 259,148 314.5,52 425.5,52"/>
      <polygon role="img" aria-label="Photo of a wooden privacy gate" fill="url(#gateBrick)" points="373,285 339.5,343 272.5,343 239,285 272.5,227 339.5,227"/>
      <polygon role="img" aria-label="Photo of a black aluminium fence on a lawn" fill="url(#blackLawn)" points="498,355 464.5,413 397.5,413 364,355 397.5,297 464.5,297"/>
      <polygon role="img" aria-label="Photo of an arched wooden gate" fill="url(#archGate)" points="389,417 353.5,478.5 282.5,478.5 247,417 282.5,355.5 353.5,355.5"/>
      <polygon role="img" aria-label="Photo of a split rail fence by a brick house" fill="url(#railBrick)" points="515,487 479.5,548.5 408.5,548.5 373,487 408.5,425.5 479.5,425.5"/>
      <polygon role="img" aria-label="Photo of a wooden privacy fence with garden shrubs" fill="url(#privacyShrubs)" points="290,500 243.5,580 150.5,580 104,500 150.5,420 243.5,420"/>
      <polygon role="img" aria-label="Photo of a wooden rail fence at the edge of a lawn" fill="url(#railLawn)" points="385,540 363,578 319,578 297,540 319,502 363,502"/>
    </g>
    <rect x="0" y="590" width="540" height="110" fill="var(--orange)"/>
  </svg>

  <div class="brand">
    <span class="brand__mark"></span>
    <div>
      <div class="brand__name">Hollowbrook Rails</div>
      <div class="brand__phone">555-014-2273</div>
    </div>
  </div>
  <p class="brand__tag">Sturdy fences, friendly neighbors, every time</p>
  <h1 class="headline">WE BUILD FENCES....</h1>
  <p class="subline">And we would love to build your fence too!</p>

  <div class="contact">
    <div class="contact__phone">555-014-2273</div>
    <div class="contact__line">office@mybraxtonyard.com</div>
    <div class="contact__line">www.MyBraxtonYard.com</div>
  </div>
</section>

<section class="sheet sheet--back" aria-label="Flyer back">
  <svg class="art" viewBox="0 0 540 700" width="540" height="700">
    <defs>
      <linearGradient id="lawnPanel" x1="0" y1="0" x2="0" y2="1">
        <stop offset="0" stop-color="#a9c4dc"/><stop offset=".18" stop-color="#3f5f35"/><stop offset=".4" stop-color="#c49a62"/><stop offset=".55" stop-color="#7aa640"/><stop offset="1" stop-color="#5e8a2c"/>
      </linearGradient>
      <linearGradient id="mapTone" x1="0" y1="0" x2="1" y2="1">
        <stop offset="0" stop-color="#efede7"/><stop offset=".5" stop-color="#e3e6df"/><stop offset="1" stop-color="#ebe8e0"/>
      </linearGradient>
    </defs>
    <polygon fill="var(--orange)" points="0,0 540,0 540,15 400,15 380,52 0,52"/>
    <polygon role="img" aria-label="Photo of a wooden privacy fence around a green lawn with a patio chair" fill="url(#lawnPanel)" stroke="#ffffff" stroke-width="4" points="400,15 545,15 545,365 400,365 318,190"/>
    <rect role="img" aria-label="Street map showing the showroom location" x="195" y="400" width="155" height="140" fill="url(#mapTone)" stroke="var(--orange)" stroke-width="2"/>
    <path class="pin" d="M268 470 c-5 -7 -8 -10 -8 -14 a8 8 0 0 1 16 0 c0 4 -3 7 -8 14 z" fill="var(--pin)"/>
    <circle cx="268" cy="456" r="3" fill="#ffffff"/>
    <polygon fill="var(--orange)" points="0,582 540,540 540,700 0,700"/>
  </svg>

  <h2 class="why">WHY CHOOSE US?</h2>
  <p class="why__sub">Beautiful, professionally installed fences<br>at affordable prices!</p>
  <ul class="perks">
    <li>Free Estimates</li>
    <li>Professional Installation</li>
    <li>Concrete in EVERY Post</li>
    <li>HOA Submission Assistance</li>
    <li>Lifetime Workmanship Warranty</li>
    <li>Experienced Installation Teams</li>
    <li>Quality Workmanship &amp; Materials</li>
    <li>FREE Gate Adjustments for LIFE</li>
  </ul>
  <h3 class="where">WHERE ARE WE?</h3>

  <div class="visit">
    <div class="visit__title">Visit our indoor &amp; outdoor showroom!</div>
    <div>48 Quarry Ln<br>Braxton, NC 28000</div>
    <div>Our outdoor showroom is open <span class="visit__big">24/7</span></div>
    <div>while our indoor showroom and office is open Monday</div>
    <div class="visit__hours">Thurs 9am - 3pm, Friday 9am - 1pm</div>
  </div>
</section>

</body>
</html>
```